Athletic Director Business Card

I need a business card that is very appealing and shows my school logo and colours (red, white and black). We just finished changing our school logo and have sent the two logos we use and I have also sent the logo W that we also use. I'm not sure if combining them works but I thought I would send it anyway and let your creative juices flow. Looking for a simple but very luring design. It could have the different sports on it but I think doing something with the logo is probably the direction I would like to see as we offer 11 different sports and 22 different teams so that might get to busy. We have a long "Tradition of Excellence" and maybe that could be on the card. If you need to change to logo by shadowing it, or making it a two colour with a glow in it or what every you think would make it look fantastic give it a try as I'm open to different looks.

Target Market(s)

Parents of high school athletes, businesses throughout our city, principals.

Industry/Entity Type

School

Requirements
Must have
• Name of School - Ridgemont Valley High School or just Ridgemont Valley.
My Name - Marcus Holloway
Position - Athletic Director
Phone - 403-555-0147
Cell - 403-555-0183
Email - mkholloway@pvsd.ab.ca
Website - www.ridgemontvalleyathletics.com

```html
<!DOCTYPE html>
<html lang="en">
<head>
<meta charset="utf-8">
<title>Athletic Director Business Card – Ridgemont Valley High School</title>
<link rel="stylesheet" href="https://fonts.googleapis.com/css2?family=Lato:wght@400;700;900&display=swap">
<style>
  :root {
    --stage: #2b2b2d;
    --team-red: #d0232b;
    --deep-red: #a5192a;
    --maroon: #8e1b22;
    --ink: #1a1a1a;
    --paper: #f4f4f4;
    --paper-shade: #e2e2e2;
    --soft-white: #f1e9e9;
  }
  * { margin: 0; padding: 0; box-sizing: border-box; }
  html, body {
    width: 1200px; height: 997px; overflow: hidden;
    background: var(--stage);
    font-family: "Lato", Arial, sans-serif;
  }
  .canvas { position: relative; width: 1200px; height: 997px; }

  .card {
    position: absolute; left: 250px; width: 700px; height: 400px;
    border-radius: 26px; overflow: hidden;
  }

  /* Front */
  .card-front {
    top: 70px;
    background: linear-gradient(135deg, #e0262f 0%, var(--team-red) 55%, #b81d26 100%);
  }
  .front-mark {
    position: absolute; left: 0; right: 0; top: 115px;
    display: flex; align-items: center; justify-content: center; gap: 22px;
  }
  .front-mark .dot {
    width: 64px; height: 64px; border-radius: 50%; background: var(--ink);
  }
  .front-mark .mark-name {
    font-weight: 900; font-size: 68px; color: var(--ink);
    text-transform: uppercase; letter-spacing: 1px;
  }
  .school-name {
    position: absolute; left: 0; right: 0; bottom: 70px; text-align: center;
    font-weight: 700; font-size: 26px; letter-spacing: 1px;
    color: var(--soft-white); text-transform: uppercase;
  }

  /* Back */
  .card-back {
    top: 527px;
    background: linear-gradient(160deg, #ffffff 0%, var(--paper) 55%, var(--paper-shade) 100%);
  }
  .team-mark {
    position: absolute; left: 44px; top: 60px;
    display: flex; align-items: center; gap: 14px;
  }
  .team-mark .dot {
    width: 46px; height: 46px; border-radius: 50%; background: var(--ink);
  }
  .team-mark .mark-name {
    font-weight: 900; font-size: 36px; color: var(--deep-red); text-transform: uppercase;
  }
  .identity {
    position: absolute; right: 44px; top: 50px; width: 240px; text-align: right;
  }
  .identity .name {
    font-size: 24px; color: var(--deep-red);
    padding-bottom: 4px; border-bottom: 2px solid var(--ink);
  }
  .identity .name strong { font-weight: 900; }
  .identity .title {
    font-size: 13px; font-weight: 700; color: var(--ink); padding-top: 5px;
  }
  .school-wordmark {
    position: absolute; right: 44px; top: 138px;
    font-weight: 900; font-size: 24px; color: var(--maroon); text-transform: uppercase;
  }
  .divider {
    position: absolute; left: 44px; right: 44px; top: 192px;
    height: 2px; background: var(--ink);
  }
  .contacts {
    position: absolute; left: 44px; top: 226px; list-style: none;
  }
  .contacts li {
    display: flex; align-items: center; gap: 14px;
    font-size: 18px; font-weight: 700; color: var(--ink); height: 34px;
  }
  .contacts svg { width: 20px; height: 20px; fill: var(--team-red); }
  .website {
    position: absolute; left: 44px; bottom: 36px;
    font-size: 19px; font-weight: 700; color: var(--ink);
  }
  .website span { color: var(--team-red); }
</style>
</head>
<body>
<main class="canvas">

  <section class="card card-front" aria-label="Business card front">
    <div class="front-mark">
      <span class="dot"></span>
      <span class="mark-name">Valley Rams</span>
    </div>
    <p class="school-name">Ridgemont Valley High School</p>
  </section>

  <section class="card card-back" aria-label="Business card back">
    <div class="team-mark">
      <span class="dot"></span>
      <span class="mark-name">Valley Rams</span>
    </div>

    <div class="identity">
      <p class="name">Trevor <strong>Lindqvist</strong></p>
      <p class="title">Athletic Director</p>
    </div>

    <p class="school-wordmark">Ridgemont Valley</p>
    <div class="divider"></div>

    <ul class="contacts">
      <li>
        <svg viewBox="0 0 24 24" aria-hidden="true"><path d="M3 9c0-3 4-5 9-5s9 2 9 5l-4 1-1-3H8L7 10 3 9zm3 3h12l2 8H4l2-8zm6 2a2.5 2.5 0 1 0 0 5 2.5 2.5 0 0 0 0-5z"/></svg>
        403-555-0147
      </li>
      <li>
        <svg viewBox="0 0 24 24" aria-hidden="true"><path d="M7 2h10a2 2 0 0 1 2 2v16a2 2 0 0 1-2 2H7a2 2 0 0 1-2-2V4a2 2 0 0 1 2-2zm0 3v13h10V5H7zm5 14.2a1 1 0 1 0 0 2 1 1 0 0 0 0-2z"/></svg>
        403-555-0183
      </li>
      <li>
        <svg viewBox="0 0 24 24" aria-hidden="true"><path d="M2 5h20v14H2V5zm2 2v.5l8 5.5 8-5.5V7H4zm0 2.9V17h16V9.9l-8 5.5-8-5.5z"/></svg>
        tjlindqvist@pvsd.ab.ca
      </li>
    </ul>

    <p class="website">www.<span>ridgemontvalleyathletics</span>.com</p>
  </section>

</main>
</body>
</html>
```